Harborline Energy - needs a business card

Harborline Energy is a U.S. based diesel sourcing and distribution company that supports American oil & gas fields through providing quality product and consistent services.

Target Market(s)

Oil and Gas

Contact Information for Business Card

The background of the card must be white to ensure the logo pops.

Font styles to use
Serif
Sans Serif

Colors

Designer to choose colors to be used in the design.

Requirements
Must have
• Front of Card: Tag line: Harborline Energy, Powering America's Oil & Gas fields.
• Not sure if you guys do this part but just in case...
• Dale Menschow
• Owner/CEO
• C:555.318.4076
• E:Dmenschow@harborlineenergy.example
• W:Harborlineenergy.example
• Locations: Servicing the Powder River, DJ basin and Bakken formations.
• Back of Card: " Frac fueling is what we do. We understand how important diesel fuel is to your operation, which is why our main service line is Frac fueling. We assure our supply and stand by our service"

```html
<!DOCTYPE html>
<html lang="en">
<head>
<meta charset="utf-8">
<title>Harborline Energy Business Card</title>
<link href="https://fonts.googleapis.com/css2?family=Exo+2:wght@400;500;600;700&display=swap" rel="stylesheet">
<style>
  :root {
    --stage: #3a3a3a;
    --card-dark: #262626;
    --card-light: #ffffff;
    --brand-red: #c1272d;
    --brand-navy: #1f3a6e;
    --ink: #2e2e2e;
    --silver: #c9c9c9;
    --paper-text: #f2f2f2;
  }
  * { margin: 0; padding: 0; box-sizing: border-box; }
  html, body {
    width: 1200px; height: 900px; overflow: hidden;
    background: var(--stage);
    font-family: "Exo 2", sans-serif;
  }
  .canvas { position: relative; width: 1200px; height: 900px; }

  .card {
    position: absolute;
    box-shadow: 0 10px 28px rgba(0,0,0,0.45);
  }

  /* Back of card */
  .card-back {
    left: 290px; top: 30px; width: 620px; height: 354px;
    background: var(--card-dark);
    display: flex; flex-direction: column; align-items: center; justify-content: center;
    text-align: center; padding: 0 50px;
  }
  .back-brand {
    display: flex; align-items: center; gap: 14px;
    color: var(--silver); font-weight: 700; font-size: 30px;
    text-transform: uppercase; letter-spacing: 1px;
  }
  .back-brand .brand-dot {
    width: 40px; height: 40px; border-radius: 50%; background: var(--silver);
  }
  .back-tagline {
    margin-top: 16px; color: var(--brand-red);
    font-size: 19px; font-weight: 500;
  }
  .back-statement {
    margin-top: 10px; color: var(--paper-text);
    font-size: 16px; line-height: 1.4;
  }

  /* Front of card */
  .card-front {
    left: 190px; top: 410px; width: 820px; height: 468px;
    background: var(--card-light);
  }
  .front-brand {
    position: absolute; left: 44px; top: 206px;
    display: flex; align-items: center; gap: 12px;
    color: var(--brand-navy); font-weight: 700; font-size: 23px;
    text-transform: uppercase; letter-spacing: 0.5px;
  }
  .front-brand .brand-dot {
    width: 46px; height: 46px; border-radius: 50%; background: var(--brand-navy);
  }
  .contact-block {
    position: absolute; left: 420px; top: 118px; width: 380px;
    color: var(--ink);
  }
  .person-name { font-size: 27px; font-weight: 400; line-height: 1.1; }
  .person-name .first { color: var(--brand-red); font-weight: 700; }
  .person-role { font-size: 19px; margin-top: 4px; }
  .service-area {
    margin-top: 18px; color: var(--brand-red);
    font-size: 20px; line-height: 1.25;
  }
  .contact-list { list-style: none; margin-top: 16px; }
  .contact-list li {
    display: flex; align-items: center; gap: 12px;
    font-size: 18px; margin-bottom: 9px;
  }
  .contact-list svg { width: 22px; height: 22px; flex: none; }
  .web .domain { color: var(--brand-navy); }
</style>
</head>
<body>
<main class="canvas">

  <section class="card card-back" aria-label="Back of card">
    <div class="back-brand"><span class="brand-dot"></span>Harborline Energy</div>
    <p class="back-tagline">Powering America's Oil &amp; Gas Fields</p>
    <p class="back-statement">Frac fueling is what we do. We understand how important diesel fuel is to your operation, which is why our main service line is Frac fueling. We assure our supply and stand by our service.</p>
  </section>

  <section class="card card-front" aria-label="Front of card">
    <div class="front-brand"><span class="brand-dot"></span>Harborline Energy</div>

    <div class="contact-block">
      <h1 class="person-name"><span class="first">Dale</span> Menschow</h1>
      <p class="person-role">Owner | CEO</p>
      <p class="service-area">Servicing the Powder River<br>DJ basin and Bakken formations</p>
      <ul class="contact-list">
        <li class="phone">
          <svg viewBox="0 0 24 24" aria-hidden="true"><path fill="#c1272d" d="M6.6 10.8a15 15 0 0 0 6.6 6.6l2.2-2.2c.3-.3.7-.4 1-.2 1.1.4 2.3.6 3.6.6.6 0 1 .4 1 1V20c0 .6-.4 1-1 1A17 17 0 0 1 3 4c0-.6.4-1 1-1h3.5c.6 0 1 .4 1 1 0 1.3.2 2.5.6 3.6.1.3 0 .7-.2 1z"/></svg>
          555 318 4076
        </li>
        <li class="email">
          <svg viewBox="0 0 24 24" aria-hidden="true"><rect x="2" y="5" width="20" height="14" rx="1.5" fill="#c1272d"/><polyline points="3,6 12,13 21,6" fill="none" stroke="#fff" stroke-width="1.6"/></svg>
          dmenschow@harborlineenergy.example
        </li>
        <li class="web">
          <svg viewBox="0 0 24 24" aria-hidden="true"><circle cx="12" cy="12" r="10" fill="#c1272d"/><g fill="none" stroke="#fff" stroke-width="1.3"><ellipse cx="12" cy="12" rx="4" ry="10"/><line x1="2" y1="12" x2="22" y2="12"/></g></svg>
          <span>www.<span class="domain">harborlineenergy</span>.example</span>
        </li>
      </ul>
    </div>
  </section>

</main>
</body>
</html>
```